Pell Haven Branding for Contracts and Customer facing documents

We are hoping to create a themed branding for our company. We would like to leverage this across our contracts, documents, and all client information and proposals. www.BuildWithPell.com is our website. We are selling high end custom homes. We am intending to use this template for a Lead Magnet and other marketing.

Target Market(s)

Luxury Custom Home Buyers

Industry/Entity Type

Residential Construction

Other font styles liked:
• You may choose, We want to be elegant but very legible and professional

Colors
0054AA
0677BA
7BADD7
CADEEF
E8F1F8

```html
<!DOCTYPE html>
<html lang="en">
<head>
<meta charset="utf-8">
<title>Pell Haven – Step 4 Design Fee</title>
<link href="https://fonts.googleapis.com/css2?family=Montserrat:wght@400;500;700;800&display=swap" rel="stylesheet">
<style>
  :root {
    --navy: #234460;
    --gold: #d8b76e;
    --beige: #dedbd0;
    --ice: #e8f1f8;
    --mist: #cadeef;
    --ink: #2b2b2b;
    --paper: #fdfdfd;
  }
  * { box-sizing: border-box; margin: 0; padding: 0; }
  html, body { width: 928px; height: 1200px; overflow: hidden; }
  body {
    position: relative;
    background: #ffffff;
    font-family: "Montserrat", sans-serif;
    color: var(--ink);
    border: 1px solid #c9c9c9;
  }
  .backdrop { position: absolute; inset: 0; }
  .content-panel {
    position: absolute; left: 85px; top: 213px; width: 780px; height: 878px;
    background: var(--paper);
  }
  .accent-tab {
    position: absolute; left: 341px; top: 118px; width: 88px; height: 17px;
    background: var(--gold);
  }
  .step-badge {
    position: absolute; left: 85px; top: 136px; width: 256px; height: 50px;
    background: var(--navy);
    color: #fff; font-weight: 800; font-size: 27px; letter-spacing: 0.5px;
    padding-left: 27px; line-height: 50px;
  }
  .step-flourish {
    position: absolute; left: 246px; top: 153px; width: 76px; height: 15px;
    border-radius: 8px;
    background: linear-gradient(90deg, #5d7590, #8a9db2, #5d7590);
    opacity: 0.8;
  }
  .page-title {
    position: absolute; right: 66px; top: 140px;
    font-size: 33px; font-weight: 800; color: var(--navy); letter-spacing: 0.6px;
  }
  .title-rule {
    position: absolute; left: 85px; top: 211px; width: 777px; height: 2px;
    background: var(--gold);
  }
  .body-copy {
    font-size: 17.3px; font-weight: 400; letter-spacing: 0.35px; color: #333;
  }
  .intro {
    position: absolute; left: 138px; top: 233px; width: 730px; line-height: 24px;
  }
  .photo {
    position: absolute; left: 138px; top: 449px; width: 287px; height: 239px;
    background: linear-gradient(135deg, #d9cbb8 0%, #eef1f3 40%, #8fb7d8 65%, #4a4540 100%);
  }
  .fee-detail {
    position: absolute; left: 451px; top: 449px; width: 410px; line-height: 21.8px;
  }
  .body-copy strong { font-weight: 700; color: #222; }
  .fee-box {
    position: absolute; left: 126px; top: 728px; width: 716px; height: 39px;
    border: 1px solid var(--gold); border-radius: 9px;
    display: flex; align-items: center; justify-content: center;
    font-size: 17.3px; font-weight: 700; color: #222; letter-spacing: 0.2px;
  }
  .agreement {
    position: absolute; left: 138px; top: 785px; width: 720px; line-height: 21.8px;
  }
  .signature-box {
    position: absolute; left: 126px; top: 915px; width: 702px; height: 145px;
    border: 1px solid var(--gold); border-radius: 11px;
  }
  .sig-row {
    position: absolute; left: 20px; height: 24px;
    font-size: 17.8px; font-weight: 400; letter-spacing: 0.3px; color: #333;
  }
  .sig-label { position: absolute; left: 0; top: 0; white-space: nowrap; }
  .sig-line {
    position: absolute; top: 16px; height: 3px;
    border-bottom: 2px dotted #444;
  }
  .sig-date { position: absolute; top: 0; white-space: nowrap; }
  .footer-band {
    position: absolute; left: 85px; top: 1090px; width: 780px; height: 19px;
    background: var(--gold);
  }
  .footer-name {
    position: absolute; left: 85px; top: 1127px;
    font-size: 16.5px; letter-spacing: 0.6px; color: #444;
  }
  .page-number {
    position: absolute; right: 62px; top: 1127px;
    font-size: 16.5px; color: #444;
  }
</style>
</head>
<body>
  <svg class="backdrop" width="928" height="1200" viewBox="0 0 928 1200" aria-hidden="true">
    <defs>
      <linearGradient id="iceBand" x1="0" y1="0" x2="1" y2="0">
        <stop offset="0" stop-color="#cadeef" stop-opacity="0.9"/>
        <stop offset="1" stop-color="#e8f1f8" stop-opacity="0.2"/>
      </linearGradient>
      <linearGradient id="iceBandRight" x1="1" y1="1" x2="0" y2="0">
        <stop offset="0" stop-color="#cadeef" stop-opacity="0.8"/>
        <stop offset="1" stop-color="#e8f1f8" stop-opacity="0"/>
      </linearGradient>
    </defs>
    <polygon points="370,0 675,0 0,820 0,420" fill="url(#iceBand)"/>
    <polygon points="215,0 245,0 0,255 0,230" fill="var(--beige)"/>
    <polygon points="165,0 230,0 125,100 110,100 0,232 0,200" fill="var(--beige)"/>
    <polygon points="350,0 372,0 195,212 176,212" fill="var(--beige)"/>
    <polygon points="928,1000 928,1200 700,1200" fill="url(#iceBandRight)"/>
  </svg>

  <div class="content-panel"></div>

  <div class="accent-tab"></div>
  <div class="step-badge">STEP 4</div>
  <div class="step-flourish" role="img" aria-label="Decorative flourish"></div>
  <h1 class="page-title">DESIGN FEE</h1>
  <div class="title-rule"></div>

  <p class="intro body-copy">It is our goal to help you reach a point where you may begin construction on your new custom home containing all of your wishes and desires. This step in the process will engage Pell Haven to create a concept and then a set of construction drawings in order to accurately price and establish a budget for your new custom home. You will be allowed one revision after the construction drawings are completed. Additional revisions and drawing time will be at an additional charge. We will advise you before we enter into additional drawing time requirements.</p>

  <div class="photo" role="img" aria-label="Photo of a person using a calculator over printed floor plan drawings"></div>

  <p class="fee-detail body-copy">Drawing fees will be set at <strong>$85.00</strong> per hour. The fee to provide this service to our clients is <strong>$10,000.00</strong> which also includes a detailed electrical plan. All of our designs are created in house, which will save you thousands of dollars in outside architectural fees. In addition, we will work with you closely to personally design your dream home. This fee is non-refundable and separate from any contract deposit required at the time of construction contract.</p>

  <div class="fee-box">Custom Home Plan Creation and Detailed Electrical Plan: $10,000.00</div>

  <p class="agreement body-copy">By Signing below and paying the appropriate fees, you agree to the terms and authorize Pell Haven to proceed with the construction drawings on your new home. In addition, you understand that no work will commence until all signatures are completed and payment is received in full.</p>

  <div class="signature-box">
    <div class="sig-row" style="top:25px; width:670px;">
      <span class="sig-label">Customer Signature(s):</span>
      <span class="sig-line" style="left:219px; width:250px;"></span>
      <span class="sig-date" style="left:475px;">Date:</span>
      <span class="sig-line" style="left:529px; width:137px;"></span>
    </div>
    <div class="sig-row" style="top:69px; width:670px;">
      <span class="sig-line" style="left:219px; width:250px;"></span>
      <span class="sig-date" style="left:475px;">Date:</span>
      <span class="sig-line" style="left:529px; width:133px;"></span>
    </div>
    <div class="sig-row" style="top:113px; width:670px;">
      <span class="sig-label">Pell Haven, LLC.:</span>
      <span class="sig-line" style="left:219px; width:250px;"></span>
      <span class="sig-date" style="left:475px;">Date:</span>
      <span class="sig-line" style="left:529px; width:133px;"></span>
    </div>
  </div>

  <div class="footer-band"></div>
  <div class="footer-name">PELL HAVEN CUSTOM HOMES</div>
  <div class="page-number">5</div>
</body>
</html>
```